B2B Umbrella Site Requires Simple, Stylish Slider Designs

We're a dynamic promotional merchandise business in the process of building a new B2B Umbrella Store. It's our goal to provide printed umbrellas to suit the needs of our clients. Our main page is in need of ONE large key banner and THREE smaller sub category banners. We would like to see designs that use grey and green (or similar) to match with the theme of our layout. See: http://canopyharbor.com.au/

The final designs should convey the desirability of our umbrellas while looking slick and modern in style. Please find attached our place holder banners for size reference and umbrella images to use in designs. If you require any further details or content, feel free to contact us.

Target Market(s)

Professionals and businesses across a wide range of fields. We offer a customisable product so we are as flexible as our target market.

Industry/Entity Type

Building

Font styles to use
Sans Serif

Requirements
Must have
• Must match sizes of attached sample graphics (
sub_banner + main_banner images). Must feature umbrella images attached to the brief - pick which images suit your design, but please ensure they are the correct umbrella style for the banner text. Clear, stylish text based on existing text found on sample graphics.
Nice to have
• Colours similar to the ones existing on the website already.
Should not have
• No serif fonts or clipart. Colours that do not facilitate easy reading.

```html
<!DOCTYPE html>
<html lang="en">
<head>
<meta charset="utf-8">
<title>CanopyHarbor – Promotional Umbrellas</title>
<link href="https://fonts.googleapis.com/css2?family=Lato:wght@400;700;900&family=Roboto:wght@400;500;700&display=swap" rel="stylesheet">
<style>
:root{
  --green:#7fbf00;
  --green-light:#94cf2a;
  --green-dark:#6fa800;
  --accent:#8cc63f;
  --ink:#333;
  --ink-soft:#555;
  --line:#cfcfcf;
  --panel:#f7f7f7;
  --panel-border:#d6d6d6;
  --btn-dark:#3b3b3b;
  --white:#fff;
}
*{box-sizing:border-box;margin:0;padding:0}
html,body{width:1200px;height:1000px;overflow:hidden;background:var(--white);font-family:"Roboto",Arial,sans-serif;color:var(--ink)}
.page{position:relative;width:1200px;height:1000px}
.rule{position:absolute;left:0;width:1200px;height:1px;background:var(--line)}
.brand{position:absolute;left:14px;top:44px;font-weight:700;font-size:38px;color:var(--green);letter-spacing:.5px;display:flex;align-items:center;gap:10px}
.brand-dot{width:18px;height:18px;border-radius:50%;background:var(--green)}
.search{position:absolute;left:519px;top:50px;display:flex;gap:4px}
.search-input{width:200px;height:32px;border:1px solid #c8c8c8;border-radius:4px;background:#fff}
.search-btn{width:79px;height:33px;border-radius:4px;background:var(--btn-dark);color:#fff;font-size:13px;font-weight:500;display:flex;align-items:center;justify-content:center}
.nav{position:absolute;left:14px;top:105px;width:1170px;height:46px;border-radius:3px;background:linear-gradient(var(--green-light),var(--green-dark));box-shadow:0 3px 5px rgba(0,0,0,.2);display:flex}
.nav-item{height:46px;padding:0 20px;display:flex;align-items:center;color:#fff;font-size:15px;border-right:1px solid rgba(255,255,255,.8)}
.panel-head{position:absolute;height:45px;background:var(--panel);border:1px solid var(--panel-border);border-radius:3px;box-shadow:0 2px 3px rgba(0,0,0,.12);padding-left:18px;display:flex;align-items:center;font-size:18px;color:var(--ink)}
.cat-list{position:absolute;left:20px;top:292px;width:256px;list-style:none}
.cat-list li{height:38px;display:flex;align-items:center;font-size:12px;font-weight:700;color:#222;border-bottom:1px dotted #555}
.cat-list li:last-child{border-bottom:none}
.field-label{position:absolute;left:20px;font-size:12px;color:var(--ink-soft)}
.field{position:absolute;left:20px;width:258px;height:32px;border:1px solid #c8c8c8;border-radius:4px;background:#fff}
.hero{position:absolute;left:314px;top:212px;width:870px;height:358px;overflow:hidden;background:linear-gradient(180deg,#8fc447 0%,#b6dc7a 35%,#9ccf55 62%,#5f8f2a 78%,#8a5a33 86%,#6b4126 100%)}
.hero-band{position:absolute;left:0;top:28px;width:870px;height:62px;background:rgba(235,245,210,.55);border-top:2px solid rgba(255,255,255,.5);border-bottom:2px solid rgba(255,255,255,.5)}
.hero-title{position:absolute;left:33px;top:44px;font-family:"Lato",sans-serif;font-weight:700;font-size:29px;color:#333;letter-spacing:.2px;white-space:nowrap}
.hero-copy{position:absolute;left:33px;top:121px;width:312px;font-family:"Lato",sans-serif;font-size:17px;line-height:22px;color:#333}
.hero-btn{position:absolute;left:33px;top:234px;width:193px;height:44px;background:linear-gradient(#fff,#dcdcdc);display:flex;align-items:center;justify-content:center;font-family:"Lato",sans-serif;font-weight:900;font-size:16px;color:#333;box-shadow:0 2px 3px rgba(0,0,0,.25)}
.hero-art{position:absolute;left:375px;top:125px;width:450px;height:225px;background:linear-gradient(100deg,rgba(170,30,35,.55),rgba(200,170,90,.55));border-radius:6px}
.sub{position:absolute;top:572px;width:289px;height:158px;overflow:hidden}
.sub-band{position:absolute;left:0;top:28px;width:289px;height:102px}
.sub-art{position:absolute;top:14px;width:100px;height:130px;border-radius:50% 50% 10px 10px}
.sub-text{position:absolute;top:36px;width:180px;text-align:center;font-family:"Lato",sans-serif;color:#fff}
.sub-text .s1{font-size:18px;font-weight:700;line-height:24px}
.sub-text .s2{font-size:28px;font-weight:700;color:var(--accent);line-height:44px}
.sub-text .s3{font-size:14px;font-weight:700;line-height:18px}
.product{position:absolute;top:850px;width:269px;height:160px;border:1px solid var(--panel-border);border-radius:3px;background:#fff}
.tag{position:absolute;left:10px;top:10px;width:40px;height:24px;background:#f2f2f2;border:1px solid #ddd;border-radius:2px;font-size:12px;color:var(--green-dark);display:flex;align-items:center;justify-content:center}
.product-img{position:absolute;left:44px;top:43px;width:181px;height:110px;background:#f4f4f4}
</style>
</head>
<body>
<div class="page">
  <div class="rule" style="top:4px"></div>

  <div class="brand"><span>CanopyHarbor</span><span class="brand-dot"></span></div>

  <div class="search"><div class="search-input"></div><div class="search-btn">Search</div></div>

  <nav class="nav">
    <div class="nav-item">Home</div>
    <div class="nav-item">Fast Delivery</div>
    <div class="nav-item">Testimonials</div>
    <div class="nav-item">Sampling</div>
    <div class="nav-item">Contact Us</div>
    <div class="nav-item">FAQ</div>
  </nav>

  <div class="rule" style="top:181px"></div>

  <div class="panel-head" style="left:14px;top:212px;width:270px">Categories</div>
  <ul class="cat-list">
    <li>Childrens Umbrellas</li>
    <li>Folding Umbrellas</li>
    <li>Medium Umbrellas</li>
    <li>Big Golf Umbrellas</li>
    <li>Beach Umbrellas</li>
    <li>Cafe Umbrellas</li>
  </ul>

  <div class="panel-head" style="left:14px;top:546px;width:270px">Enquiry</div>
  <div class="field-label" style="top:640px">Name:</div>
  <div class="field" style="top:671px"></div>
  <div class="field-label" style="top:717px">Phone:</div>
  <div class="field" style="top:748px"></div>
  <div class="field-label" style="top:794px">Email:</div>
  <div class="field" style="top:825px"></div>
  <div class="field-label" style="top:871px">Product Detail:</div>
  <div class="field" style="top:902px;height:80px"></div>

  <section class="hero" role="img" aria-label="Photo of green grass on a wooden deck background">
    <div class="hero-band"></div>
    <div class="hero-title">AUSTRALIAS TOP PROMOTIONAL UMBRELLA VENDOR</div>
    <div class="hero-copy">Massive selection of umbrellas in stock and ready to be printed with your logo or slogan.</div>
    <div class="hero-btn">VIEW ALL PRODUCTS</div>
    <div class="hero-art" role="img" aria-label="Photo of a red and a beige golf umbrella standing open"></div>
  </section>

  <section class="sub" style="left:314px;background:#6a6a6a">
    <div class="sub-band" style="background:#474747"></div>
    <div class="sub-art" style="left:184px;background:#5a1a14" role="img" aria-label="Photo of a dark red medium umbrella"></div>
    <div class="sub-text" style="left:2px"><div class="s1">MEDIUM</div><div class="s2">CORPORATE</div><div class="s3">UMBRELLAS</div></div>
  </section>
  <section class="sub" style="left:605px;background:#7a6a00">
    <div class="sub-band" style="background:#4d4300"></div>
    <div class="sub-art" style="left:186px;background:#d42a22" role="img" aria-label="Photo of a red folding umbrella"></div>
    <div class="sub-text" style="left:6px"><div class="s1">PORTABLE</div><div class="s2">FOLDING</div><div class="s3">UMBRELLAS</div></div>
  </section>
  <section class="sub" style="left:896px;background:#23882a">
    <div class="sub-band" style="background:#0c4a18"></div>
    <div class="sub-art" style="left:172px;background:linear-gradient(90deg,#f0f0f0,#1e6a2a)" role="img" aria-label="Photo of a white and green golf umbrella"></div>
    <div class="sub-text" style="left:-8px"><div class="s1">POPULAR</div><div class="s2">GOLF</div><div class="s3">UMBRELLAS</div></div>
  </section>

  <div class="panel-head" style="left:314px;top:778px;width:870px;height:44px">New Products</div>

  <div class="product" style="left:314px"><div class="tag">New</div><div class="product-img" role="img" aria-label="Product image placeholder"></div></div>
  <div class="product" style="left:613px"><div class="tag">New</div><div class="product-img" role="img" aria-label="Product image placeholder"></div></div>
  <div class="product" style="left:913px"><div class="tag">New</div><div class="product-img" role="img" aria-label="Product image placeholder"></div></div>
</div>
</body>
</html>
```